Beauty Therapy Web Design

I need a web page design for a small beauty therapy clinic, the owner is currently the only beauty therapist working there.
We require the following pages:
Home
About
Treatments
Nails
Courses
Contact
I will attach the clinics business card, treatment menu and signage so that you get a feeling for the branding colours etc.
This is the first website for the beauty therapist, she would like to attract new clients and also tourists that come in on the cruise ships. The thing that sets her apart from other clinics is that she welcomes texting for appointments.
I have selected refundable because I have never done this before so I don't know what to expect, I have the full intention of going through with it as long as I get a good design.
Feel free to ask for further information
Reason: Project extended as I am away for work and am unable to meet with the owner.
Target Market(s)
Females 18 to 50
Industry/Entity Type
Business
Look and feel
Each slider illustrates characteristics of the customer's brand and the style your logo design should communicate.

```html
<!DOCTYPE html>
<html lang="en">
<head>
<meta charset="utf-8">
<title>Lumiera Beauty Therapy – Treatments</title>
<link rel="stylesheet" href="https://fonts.googleapis.com/css2?family=Carlito:wght@400;700&family=Cormorant+Garamond:ital,wght@1,500;1,600&display=swap">
<style>
:root{
  --purple:#6b5799;
  --gold:#c29f47;
  --white:#ffffff;
  --text:#6b5799;
  --rule:#7a68a6;
}
*{margin:0;padding:0;box-sizing:border-box}
html,body{width:1200px;height:1000px;overflow:hidden;background:var(--white)}
body{position:relative;font-family:"Carlito",Calibri,sans-serif;color:var(--text)}
.site-header{position:absolute;left:0;top:0;width:1200px;height:203px;background:var(--purple)}
.booking-line{position:absolute;right:125px;top:18px;font-family:"Cormorant Garamond",serif;font-style:italic;font-weight:500;font-size:19px;color:var(--gold)}
.brand{position:absolute;left:124px;top:60px;font-family:"Carlito",Calibri,sans-serif;font-weight:400;font-size:44px;line-height:1.1;color:var(--gold)}
.brand-sub{display:block;font-size:44px}
.main-nav{position:absolute;right:120px;top:150px;display:flex;gap:0}
.main-nav a{font-size:20px;color:var(--white);text-decoration:none;padding:4px 12px;border-radius:8px;line-height:24px}
.main-nav a.is-active{background:var(--gold)}
.section-title{position:absolute;font-family:"Cormorant Garamond",serif;font-style:italic;font-weight:600;font-size:29px;color:var(--gold)}
.intro{position:absolute;font-size:16px;line-height:20px;color:var(--text)}
.rule{position:absolute;height:1px;background:var(--rule)}
.price-card{position:absolute;width:294px;border:3px solid var(--purple);border-top:none;border-radius:0 0 3px 3px}
.price-card h3{height:41px;background:var(--purple);margin:0 -3px;padding-left:7px;font-family:"Cormorant Garamond",serif;font-style:italic;font-weight:500;font-size:27px;line-height:41px;color:var(--gold)}
.price-table{display:grid;font-weight:700;font-size:18.5px;line-height:25px;position:relative}
.price-table .names{padding:12px 0 14px 4px}
.price-table .prices{padding:12px 0 14px 17px;border-left:1px solid var(--purple)}
.text-book{position:absolute;left:775px;top:727px;width:291px;height:40px;background:var(--purple);border-radius:9px;color:var(--white);font-size:16px;line-height:40px;padding-left:8px}
.site-footer{position:absolute;left:0;top:936px;width:1200px;height:64px;background:var(--purple);color:var(--white);font-size:13.5px}
.footer-nav{position:absolute;left:107px;top:23px;display:flex;gap:17px}
.footer-nav a{color:var(--white);text-decoration:none}
.copyright{position:absolute;right:140px;top:26px}
</style>
</head>
<body>
<header class="site-header">
  <div class="booking-line">Book Your Treaments, Call or Text: 07 555 0142 / 021 555 0187</div>
  <div class="brand">Lumiera<span class="brand-sub">Beauty Therapy</span></div>
  <nav class="main-nav">
    <a href="#">Home</a><a href="#">About</a><a href="#">Nails</a><a href="#" class="is-active">Treatments</a><a href="#">Courses</a><a href="#">Contact</a>
  </nav>
</header>

<main>
  <h1 class="section-title" style="left:110px;top:218px">Available Treatments</h1>
  <p class="intro" style="left:110px;top:268px">Below is a selection of treatments available at Lumiera Beauty Therapy.<br>To book a teatment please call or text 07 555 0142 or 021 555 0187</p>
  <div class="rule" style="left:112px;top:328px;width:951px"></div>

  <h2 class="section-title" style="left:110px;top:346px">Nails</h2>
  <p class="intro" style="left:107px;top:397px">We have a range of nail treatments availble including pedicures and manicures</p>

  <section class="price-card" style="left:107px;top:450px">
    <h3>Pedicure</h3>
    <div class="price-table" style="grid-template-columns:196px 1fr">
      <div class="names">Classic - 45 min<br>Deluxe - 60 min<br>Spa Delux - 75 min<br>(Includes Paraffic Dip )<br>Nail Shape<br>Nail Paint<br>French Polish<br>Sen Citizens Nail Trea-<br>tment (Ladies &amp; Gentl-<br>emen)</div>
      <div class="prices">$45.00<br>$60.00<br>$75.00<br><br>$10.00<br>$10.00<br>$15.00<br>$25.00</div>
    </div>
  </section>

  <section class="price-card" style="left:442px;top:450px">
    <h3>Manicure</h3>
    <div class="price-table" style="grid-template-columns:196px 1fr">
      <div class="names">Classic - 45 min<br>Deluxe - 60 min<br>Spa Delux - 75 min<br>(Includes Paraffic Dip )<br>Nail Shape<br>Nail Paint<br>French Polish</div>
      <div class="prices">$35.00<br>$50.00<br>$60.00<br><br>$10.00<br>$10.00<br>$15.00</div>
    </div>
  </section>

  <section class="price-card" style="left:774px;top:450px">
    <h3>Nail Enhancement</h3>
    <div class="price-table" style="grid-template-columns:196px 1fr">
      <div class="names">Acrylic or Gel Full Set<br>Pink Backfill<br>Pink &amp; White Backfill<br>Acrylic Toe Nails<br>Gel Toe Nails<br>Acrylic Nail Removal</div>
      <div class="prices">$70.00<br>$40.00<br>$50.00<br>$65.00<br>$25.00<br>$40.00</div>
    </div>
  </section>

  <a class="text-book">Book Treatment By Text: 07 555 0142</a>

  <div class="rule" style="left:108px;top:805px;width:951px"></div>
  <h2 class="section-title" style="left:104px;top:822px">Wax and Massage</h2>
  <p class="intro" style="left:101px;top:872px">We offer a variety of waxing and massages for men and women</p>
</main>

<footer class="site-footer">
  <nav class="footer-nav">
    <a href="#">Home</a><a href="#">About</a><a href="#">Nails</a><a href="#">Treatments</a><a href="#">Courses</a><a href="#">Contact</a><a href="#">Site Map</a>
  </nav>
  <div class="copyright">© Copyright Lumiera Beauty Therapy 2012</div>
</footer>
</body>
</html>
```